Business card

We are looking for a creative person to deigns our company business card.

Target Market(s)

College age student

Industry/Entity Type

Accommodation

Contact Information for Business Card

We want a fun, clean and sophisticated design. It should look good, but more importantly the information should be legible.

Font styles to use
Serif
Sans Serif
Other font styles liked:
• Open Sans ,

Colors
33a6d7

Requirements
Must have
• Must have a young and memorable message. Be legible.
• Our logo on the back on a solid blue , please find color and logo attached
• LodgeBridgely.net on the back.
Nice to have
• I would like to have couple of different fonts on the LodgeBridgely.net on the back of the cards with a solid blue.

```html
<!DOCTYPE html>
<html lang="en">
<head>
<meta charset="utf-8">
<title>LodgeBridgely.net business card</title>
<link href="https://fonts.googleapis.com/css2?family=Open+Sans:wght@400;600;700&display=swap" rel="stylesheet">
<style>
  :root {
    --brand-blue: #33a6d7;
    --deep-blue: #0f5a8c;
    --navy: #0b4a78;
    --paper: #f7f7f7;
    --ink: #3c3c3c;
    --stage: #d9dde0;
    --rule: #c9cdd0;
  }
  * { margin: 0; padding: 0; box-sizing: border-box; }
  html, body { width: 1200px; height: 786px; overflow: hidden; }
  body {
    background: var(--stage);
    font-family: "Open Sans", Arial, sans-serif;
    position: relative;
  }
  .card {
    position: absolute;
    top: 250px;
    width: 500px;
    height: 286px;
    border-radius: 18px;
    overflow: hidden;
    box-shadow: 0 10px 28px rgba(0,0,0,0.18);
  }
  .card-front { left: 60px; background: var(--paper); }
  .card-back { left: 640px; background: var(--deep-blue); }

  .front-swoosh { position: absolute; inset: 0; width: 100%; height: 100%; }

  .brand-block {
    position: absolute;
    left: 34px;
    top: 78px;
    width: 190px;
    display: flex;
    align-items: center;
    gap: 10px;
  }
  .brand-dot {
    width: 22px; height: 22px; border-radius: 50%;
    background: var(--brand-blue);
    flex: none;
  }
  .brand-name {
    font-weight: 700;
    font-size: 22px;
    color: var(--navy);
    letter-spacing: -0.3px;
  }
  .divider {
    position: absolute;
    left: 240px;
    top: 40px;
    width: 1px;
    height: 120px;
    background: var(--rule);
  }
  .contact {
    position: absolute;
    left: 262px;
    top: 44px;
    color: var(--ink);
    font-size: 12.5px;
    line-height: 1.55;
  }
  .contact-name {
    color: var(--brand-blue);
    font-weight: 700;
    font-size: 16px;
    letter-spacing: 0.3px;
    margin-bottom: 6px;
  }
  .contact-row { display: flex; align-items: center; gap: 8px; }
  .contact-row svg { width: 11px; height: 11px; flex: none; }
  .contact-address { margin-top: 6px; padding-left: 0; }

  .back-content {
    position: absolute; inset: 0;
    display: flex; flex-direction: column;
    align-items: center; justify-content: center;
    gap: 14px;
  }
  .back-name {
    display: flex; align-items: center; gap: 10px;
    font-weight: 700; font-size: 30px;
    color: var(--brand-blue);
  }
  .back-name .brand-dot { width: 26px; height: 26px; }
  .back-url {
    color: #ffffff;
    font-size: 13px;
    letter-spacing: 0.6px;
  }
</style>
</head>
<body>
  <section class="card card-front" aria-label="Card front">
    <svg class="front-swoosh" viewBox="0 0 500 286" preserveAspectRatio="none" aria-hidden="true">
      <path d="M0,168 C120,210 250,214 345,286 L0,286 Z" fill="var(--brand-blue)"/>
      <path d="M0,176 C118,218 246,224 332,286 L0,286 Z" fill="#e6e8ea"/>
      <path d="M0,186 C116,228 240,236 318,286 L0,286 Z" fill="var(--brand-blue)"/>
      <path d="M0,200 C112,242 230,252 296,286 L0,286 Z" fill="var(--navy)"/>
    </svg>

    <div class="brand-block">
      <span class="brand-dot"></span>
      <span class="brand-name">LodgeBridgely</span>
    </div>

    <div class="divider"></div>

    <div class="contact">
      <div class="contact-name">JORDAN ELLERY</div>
      <div class="contact-row">
        <svg viewBox="0 0 12 12"><rect x="3" y="0.5" width="6" height="11" rx="1.2" fill="none" stroke="var(--brand-blue)" stroke-width="1.3"/></svg>
        <span>555-210-4837</span>
      </div>
      <div class="contact-row">
        <svg viewBox="0 0 12 12"><path d="M2.5 1 L4.5 1 L5.5 3.6 L4.2 4.6 C4.9 6.2 5.8 7.1 7.4 7.8 L8.4 6.5 L11 7.5 L11 9.5 C11 10.4 10.3 11 9.4 11 C5 10.6 1.4 7 1 2.6 C1 1.7 1.6 1 2.5 1 Z" fill="var(--brand-blue)"/></svg>
        <span>555-210-4838</span>
      </div>
      <div class="contact-row">
        <svg viewBox="0 0 12 12"><rect x="0.7" y="2.2" width="10.6" height="7.6" fill="none" stroke="var(--brand-blue)" stroke-width="1.2"/><path d="M0.7 2.4 L6 6.6 L11.3 2.4" fill="none" stroke="var(--brand-blue)" stroke-width="1.2"/></svg>
        <span>info@lodgebridgely.net</span>
      </div>
      <div class="contact-row">
        <svg viewBox="0 0 12 12"><circle cx="6" cy="6" r="5.2" fill="none" stroke="var(--brand-blue)" stroke-width="1.1"/><ellipse cx="6" cy="6" rx="2.3" ry="5.2" fill="none" stroke="var(--brand-blue)" stroke-width="1"/><path d="M0.8 6 H11.2" stroke="var(--brand-blue)" stroke-width="1"/></svg>
        <span>www.lodgebridgely.net</span>
      </div>
      <div class="contact-address">407 Alder Glen<br>Dr. Larkfield, TN 30418</div>
    </div>
  </section>

  <section class="card card-back" aria-label="Card back">
    <div class="back-content">
      <div class="back-name"><span class="brand-dot"></span><span>LodgeBridgely</span></div>
      <div class="back-url">www.lodgebridgely.net</div>
    </div>
  </section>
</body>
</html>
```